Plakat-Design für Online-Vertrieb von Messeständen an Unternehmen
Zielgruppe
Wir verkaufen über unseren Onlineshop (www.standwerk-beispiel.de) Messestände an Unternehmen.
Aufgabenstellung
Wir benötigten eine Grafik, die auf unseren Messeständen als Beispiel eingebunden werden kann. Sie soll unseren Kunden die Möglichkeit geben, dass sie sich das System besser vorstellen können. Da wir das System RAVOK nennen werden, befindet sich das dazugehörige Logo in der Anlage. Das Logo sollte auf dem Design sichtbar sein, aber muss nicht im Vordergrund stehen.
Das Messesystem ist variabel und in vielen verschiedenen Breiten und Formationen aufstellbar. Die Grafik muss bei Eckständen auch mal um die Ecke laufen. Somit wäre es perfekt, wenn die Grafik für verschiedene Breiten erweiterbar wäre. Die Standardhöhe des Systems liegt immer bei 2,5m.
Zwei Beispielvarianten mit blanko Grafik liegen in der Anlage und können gerne für die Visualisierung verwendet werden.
Gerne kann auch ein einfacher Farbverlauf mit modernen Farben verwendet werden. Wir sind hier aber sehr flexibel.
Die Messestände haben eine LED-Hinterleuchtung in ihren Motiven, sodass sie in Realität strahlend wirken.
Wenn wir ein Motiv finden würden, mit dem wir den 'Strahleffekt' gut visualisieren könnten, wäre das natürlich hervorragend.
Im folgenden finden Sie andere Beispiele von Messeständen inkl. Stoffgrafiken. Hier sieht man auch die variablen Standgrößen, welche eine Erweiterbarkeit des Motivs erforderlich machen.
Fast identisch zu unserem neuen System sind die Artikel in der Kategorie 'LED Messestand Stoff' (https://www.standwerk-beispiel.de/Messestand/LED-Messestand-Stoff/)
Ansonsten sind hier aber noch weitere Beispiele:
https://www.standwerk-beispiel.de/Messestand/Messestand-Stoff/
https://www.standwerk-beispiel.de/Messestand/LED-Messestand-Stoff/
https://www.standwerk-beispiel.de/Messebausysteme/TORVANE-MO/
https://www.standwerk-beispiel.de/Messebausysteme/Quorin/Quorin-BildFront/
https://www.standwerk-beispiel.de/Messebausysteme/Quorin/Quorin-WeitTuch/

```html
<!DOCTYPE html>
<html lang="de">
<head>
<meta charset="utf-8">
<title>RAVOK – Messestand Motiv</title>
<link rel="stylesheet" href="https://fonts.googleapis.com/css2?family=Oswald:wght@500&display=swap">
<style>
  :root {
    --night: #050302;
    --ember: #3a1c06;
    --amber: #9a5a12;
    --gold: #e0a63a;
    --glow: #fbe7a6;
    --brand: #f4b01e;
  }
  html, body {
    margin: 0;
    padding: 0;
    width: 1200px;
    height: 600px;
    overflow: hidden;
    background: var(--night);
  }
  .poster {
    position: relative;
    width: 1200px;
    height: 600px;
    overflow: hidden;
  }
  .hero-visual {
    position: absolute;
    inset: 0;
    background:
      radial-gradient(ellipse 220px 300px at 1010px 300px, var(--gold) 0%, rgba(224,166,58,0.55) 45%, rgba(154,90,18,0) 100%),
      radial-gradient(ellipse 260px 140px at 620px 360px, rgba(224,166,58,0.75) 0%, rgba(154,90,18,0) 100%),
      radial-gradient(ellipse 520px 220px at 420px 560px, rgba(251,231,166,0.55) 0%, rgba(154,90,18,0.5) 40%, rgba(58,28,6,0) 100%),
      radial-gradient(ellipse 700px 360px at 700px 480px, var(--amber) 0%, var(--ember) 55%, rgba(5,3,2,0) 100%),
      linear-gradient(160deg, var(--night) 0%, var(--night) 35%, var(--ember) 100%);
  }
  .brand {
    position: absolute;
    left: 563px;
    top: 192px;
    display: flex;
    align-items: center;
    gap: 10px;
  }
  .brand-mark {
    width: 14px;
    height: 14px;
    background: var(--brand);
  }
  .brand-name {
    font-family: "Oswald", sans-serif;
    font-weight: 500;
    font-size: 64px;
    line-height: 1;
    letter-spacing: 2px;
    color: var(--brand);
  }
</style>
</head>
<body>
  <main class="poster">
    <div class="hero-visual" role="img" aria-label="Foto einer Frau mit goldener Körperfarbe im Profil, die Hand ausgestreckt, vor schwarzem Hintergrund mit goldenen Lichtreflexen und Funkeln"></div>
    <div class="brand">
      <span class="brand-name">RAVOK</span>
      <span class="brand-mark"></span>
    </div>
  </main>
</body>
</html>
```